Logo and Double sided business card

We need a logo and business card for a Point of Sale Business, Website is www.kestreltill.com.au - this is being worked on at the moment. There is a logo on the website - but this is more of a placement /logo and needs to be redesigned.
The address for Details for the Business card are

Person Name
KESTREL TILL
17/3 Worrigal Pde
Larkfield 2187
Ph 1300 585 926 (1300 KTL 926)
Email : Person@kestreltill.com.au
Web: www.kestreltill.com.au

Our company will be a Point of Sale installation and Support business. We Specialise in the Vandrel Quill system.

We do
Installation of POS Systems
Support and Maintenance of existing POS
Quill POS support
Updates

Target Market(s)

Restaurants, hotels, retail shops

Industry/Entity Type

Business

Contact Information for Business Card

Person Name
KESTREL TILL
17/3 Worrigal Pde
Larkfield 2187
Web: www.kestreltill.com.au

Logo Text

Kestrel Till

Font styles to use
Serif

Requirements
Must have
• We must have the source graphics in editable formats for both logo and business card.

```html
<!DOCTYPE html>
<html lang="en">
<head>
<meta charset="utf-8">
<title>Kestrel Till – Business Card</title>
<link rel="stylesheet" href="https://fonts.googleapis.com/css2?family=Open+Sans:wght@400;600&display=swap">
<style>
  :root {
    --backdrop: #3a332f;
    --card: #141414;
    --card-edge: #1d1d1d;
    --gold: #e39a2d;
    --ink-light: #f2f2f2;
    --card-w: 520px;
    --card-h: 300px;
  }
  * { box-sizing: border-box; margin: 0; padding: 0; }
  html, body {
    width: 1200px; height: 780px; overflow: hidden;
    background: var(--backdrop);
    font-family: "Open Sans", Arial, sans-serif;
  }
  .canvas { position: relative; width: 1200px; height: 780px; }
  .card {
    position: absolute;
    width: var(--card-w); height: var(--card-h);
    background: var(--card);
    border: 1px solid var(--card-edge);
    border-radius: 4px;
    box-shadow: 0 14px 30px rgba(0,0,0,.45);
  }
  .card--front { left: 60px; top: 110px; }
  .card--back { left: 620px; top: 370px; }

  .brand { display: flex; align-items: center; gap: 14px; color: var(--gold); white-space: nowrap; }
  .brand__mark { width: 26px; height: 26px; background: var(--gold); flex: none; }
  .brand__name { font-weight: 400; letter-spacing: .5px; }

  .card--front .brand {
    position: absolute; left: 50%; top: 50%;
    transform: translate(-50%, -50%);
  }
  .card--front .brand__name { font-size: 40px; }

  .card--back .brand {
    position: absolute; left: 130px; top: 60px;
  }
  .card--back .brand__name { font-size: 34px; }

  .details {
    position: absolute; left: 28px; top: 150px; right: 20px;
    display: flex; align-items: stretch;
  }
  .details__person {
    width: 180px; padding-right: 16px; text-align: right;
  }
  .details__name { color: var(--gold); font-size: 21px; line-height: 1.2; margin-bottom: 4px; white-space: nowrap; }
  .details__address { color: var(--ink-light); font-size: 14px; line-height: 1.35; }
  .details__rule { width: 2px; background: var(--gold); flex: none; }
  .contact-list { list-style: none; padding-left: 16px; display: flex; flex-direction: column; gap: 6px; justify-content: center; }
  .contact-list__item { display: flex; align-items: center; gap: 9px; color: var(--ink-light); font-size: 14px; white-space: nowrap; }
  .contact-list__icon {
    width: 17px; height: 17px; border-radius: 3px; background: var(--gold);
    display: flex; align-items: center; justify-content: center; flex: none;
  }
  .contact-list__icon svg { width: 11px; height: 11px; }
</style>
</head>
<body>
<main class="canvas">
  <section class="card card--front" aria-label="Card front">
    <div class="brand">
      <span class="brand__mark"></span>
      <span class="brand__name">Kestrel Till</span>
    </div>
  </section>

  <section class="card card--back" aria-label="Card back">
    <div class="brand">
      <span class="brand__mark"></span>
      <span class="brand__name">Kestrel Till</span>
    </div>
    <div class="details">
      <div class="details__person">
        <p class="details__name">Alex Harlow</p>
        <p class="details__address">17/3 Worrigal Pde<br>Larkfield 2187</p>
      </div>
      <div class="details__rule"></div>
      <ul class="contact-list">
        <li class="contact-list__item">
          <span class="contact-list__icon"><svg viewBox="0 0 12 12"><path d="M3 1h2l1 3-1.5 1a6 6 0 0 0 2.5 2.5L8 6l3 1v2c0 1-1 2-2 2A8 8 0 0 1 1 3c0-1 1-2 2-2z" fill="#141414"/></svg></span>
          1300 585 926 (1300 KTL 926)
        </li>
        <li class="contact-list__item">
          <span class="contact-list__icon"><svg viewBox="0 0 12 12"><rect x="1" y="2.5" width="10" height="7" fill="#141414"/><path d="M1 2.5l5 4 5-4" stroke="#e39a2d" fill="none"/></svg></span>
          Person@kestreltill.com.au
        </li>
        <li class="contact-list__item">
          <span class="contact-list__icon"><svg viewBox="0 0 12 12"><circle cx="6" cy="6" r="5" fill="none" stroke="#141414" stroke-width="1.2"/><path d="M1 6h10M6 1c-2.5 3-2.5 7 0 10M6 1c2.5 3 2.5 7 0 10" fill="none" stroke="#141414" stroke-width="1"/></svg></span>
          www.kestreltill.com.au
        </li>
      </ul>
    </div>
  </section>
</main>
</body>
</html>
```